Grand Opening Banner needed for Marvelous Carpets and Home

My website is www.MarvelousCarpetsandHome.com (login with password 'plorka')

A full page banner 1000px X 500px with bright, lively colors and wording that shows an exciting GRAND OPENING celebration throughout the site. Banner needs to convey the following...

Grand Opening Sale
Runs through end of the month
Savings in every department
30 day Returns
Free Rug Pads with every rug
Free shipping.

Banner can be a simple background with graphics and text, or can be a room scene with rugs and furniture, or a grouping of rugs with text.

Some Ideas and Images can be taken from our vendor's websites, such as:

http://tbvendora.com/
http://dosmir.com/dosmir_2015/
http://www.pqmats.com/
http://zaverto.com/
http://shopbelwyn.com/

I also have quite a few room scene images available for use, if you desire.

Target Market(s)

Affluent women who care about stylish decor for their homes

Industry/Entity Type

Home And Garden

Requirements
Must have
• bold, vibrant appearance. Text that can be modified in Photoshop.
Nice to have
• HAND DRAWN, ARTIST STYLE ARTWORK IS GREATLY APPRECIATED.
• flat graphics and text with little to no 3 dimensional (shadow) effect. Font styles should be elegant/luxurious. An organic, scribbled, or painted style is nice in keeping with the handmade products that we sell.
• I am open to changing the color scheme of the website, to match your banner, so don't feel tied down to my existing colors.
Should not have
• nothing too modern or extreme in style.

```html
<!DOCTYPE html>
<html lang="en">
<head>
<meta charset="utf-8">
<title>Grand Opening Sale</title>
<link rel="stylesheet" href="https://fonts.googleapis.com/css2?family=Kaushan+Script&family=Caveat+Brush&family=Roboto:wght@400&display=swap">
<style>
  :root {
    --brand-red: #9b1100;
    --text-red: #9a1204;
    --white: #ffffff;
    --deco-tint: rgba(255, 255, 255, 0.14);
  }
  html, body {
    margin: 0;
    padding: 0;
    overflow: hidden;
    background: var(--white);
  }
  .banner {
    position: relative;
    width: 1200px;
    height: 600px;
    overflow: hidden;
    background: var(--white);
    font-family: "Roboto", Arial, sans-serif;
  }
  .hero {
    position: absolute;
    left: 0;
    top: 0;
    width: 1200px;
    height: 410px;
    background: var(--brand-red);
    color: var(--white);
  }
  .hero__title {
    position: absolute;
    left: 0;
    right: 0;
    top: 18px;
    margin: 0;
    text-align: center;
    font-family: "Kaushan Script", cursive;
    font-weight: 400;
    font-size: 100px;
    line-height: 140px;
    letter-spacing: 0.5px;
    white-space: nowrap;
  }
  .hero__dates {
    position: absolute;
    left: 0;
    right: 0;
    top: 173px;
    margin: 0;
    text-align: center;
    font-size: 41px;
    line-height: 50px;
    letter-spacing: 0.5px;
    white-space: nowrap;
  }
  .hero__divider {
    position: absolute;
    left: 246px;
    top: 240px;
  }
  .hero__savings {
    position: absolute;
    left: 0;
    right: 0;
    top: 258px;
    margin: 0;
    text-align: center;
    font-family: "Caveat Brush", cursive;
    font-weight: 400;
    font-size: 66px;
    line-height: 76px;
    text-transform: uppercase;
    letter-spacing: 0.5px;
    white-space: nowrap;
    transform: scaleX(0.74);
    transform-origin: 600px 0;
  }
  .hero__cta {
    position: absolute;
    left: 559px;
    top: 348px;
    width: 140px;
    height: 52px;
    box-sizing: border-box;
    border: 1.5px solid var(--white);
    display: flex;
    align-items: center;
    justify-content: center;
  }
  .rug-motif {
    position: absolute;
    background: var(--deco-tint);
  }
  .rug-motif--round { border-radius: 50%; }
  .perks {
    position: absolute;
    left: 0;
    right: 0;
    top: 430px;
    margin: 0;
    padding: 0;
    list-style: none;
    text-align: center;
    color: var(--text-red);
    font-size: 41px;
    letter-spacing: 0.5px;
    white-space: nowrap;
  }
  .perks__item { line-height: 48px; }
  .perks__item--first { margin-bottom: 12px; }
</style>
</head>
<body>
  <main class="banner">
    <section class="hero">
      <div class="rug-motif" style="left:36px;top:0;width:78px;height:48px;transform:rotate(-20deg);" role="img" aria-label="Hand drawn rug outline"></div>
      <div class="rug-motif rug-motif--round" style="left:-12px;top:94px;width:72px;height:72px;" role="img" aria-label="Hand drawn round medallion rug"></div>
      <div class="rug-motif" style="left:-10px;top:262px;width:90px;height:60px;transform:rotate(-35deg);" role="img" aria-label="Hand drawn rug outline"></div>
      <div class="rug-motif" style="left:12px;top:340px;width:90px;height:50px;transform:rotate(-35deg);" role="img" aria-label="Hand drawn fringed rug"></div>
      <div class="rug-motif rug-motif--round" style="left:1060px;top:-30px;width:80px;height:66px;" role="img" aria-label="Hand drawn round medallion rug"></div>
      <div class="rug-motif" style="left:1138px;top:60px;width:80px;height:86px;transform:rotate(-35deg);" role="img" aria-label="Hand drawn fringed rug"></div>
      <div class="rug-motif" style="left:1144px;top:180px;width:80px;height:90px;transform:rotate(-35deg);" role="img" aria-label="Hand drawn patterned rug"></div>
      <div class="rug-motif" style="left:1148px;top:314px;width:70px;height:76px;transform:rotate(-35deg);" role="img" aria-label="Hand drawn patterned rug"></div>

      <h1 class="hero__title">Grand Opening Sale</h1>
      <p class="hero__dates">RUNS THROUGH END OF THE MONTH</p>
      <svg class="hero__divider" width="750" height="8" viewBox="0 0 750 8" aria-hidden="true">
        <line x1="0" y1="4" x2="750" y2="4" stroke="#ffffff" stroke-width="2" stroke-dasharray="34 6 3 6 48 6 3 6"/>
      </svg>
      <p class="hero__savings">Savings in every department</p>
      <a class="hero__cta" href="#" aria-label="Shop the sale">
        <svg width="46" height="34" viewBox="0 0 46 34" aria-hidden="true">
          <polyline points="4,2 20,17 4,32" fill="none" stroke="#ffffff" stroke-width="1.5"/>
          <polyline points="22,2 38,17 22,32" fill="none" stroke="#ffffff" stroke-width="1.5"/>
        </svg>
      </a>
    </section>

    <ul class="perks">
      <li class="perks__item perks__item--first">30 DAY RETURNS</li>
      <li class="perks__item">FREE RUG PADS WITH EVERY RUG</li>
      <li class="perks__item">FREE SHIPPING</li>
    </ul>
  </main>
</body>
</html>
```